Billboard

we want our Kite & Clover logo really big, we need this to stand out

Use a really bold font for the wording as it's on a billboard on the highway

Kite & Clover Logo
perhaps on left hand side really large then have a slanting line and a different colour background for the other side.

Wording BELOW-bold

TOUR NOW

kiteandclover.edu.au

Use one image,
I have attached other designs we have been using for our campaign so a similar look would be great.
specs- 1224 W × 324 H px JPEG

Target Market(s)
families

Industry/Entity Type
childcare

Target Market(s)

families

Industry/Entity Type

childcare

Requirements
Must have
• bold font and big logo

```html
<!DOCTYPE html>
<html lang="en">
<head>
<meta charset="utf-8">
<title>Kite &amp; Clover — Billboard</title>
<link rel="stylesheet" href="https://fonts.googleapis.com/css2?family=Archivo+Black&family=Montserrat:wght@900&family=Roboto+Condensed:wght@800&display=swap">
<style>
  :root {
    --page-bg: #d9d9d9;
    --sky-blue: #00aeef;
    --navy: #0d2a78;
    --navy-deep: #0a2163;
    --sun-yellow: #fff200;
    --signal-red: #ef4136;
    --white: #ffffff;
    --photo-warm: #c9a078;
    --photo-light: #e9d2b0;
    --photo-teal: #3a8fa8;
  }
  html, body {
    margin: 0;
    padding: 0;
    width: 996px;
    height: 1200px;
    overflow: hidden;
    background: var(--page-bg);
  }
  .canvas {
    width: 996px;
    height: 1200px;
    display: flex;
    align-items: center;
    justify-content: center;
  }
  .billboard {
    width: 940px;
    height: 255px;
    display: block;
    box-shadow: 0 4px 10px rgba(0, 0, 0, 0.25);
  }
  .panel-photo-stop-a { stop-color: var(--photo-light); }
  .panel-photo-stop-b { stop-color: var(--photo-warm); }
  .panel-photo-stop-c { stop-color: var(--photo-teal); }
  .panel-brand { fill: var(--sky-blue); }
  .panel-offer { fill: var(--navy); }
  .panel-offer-glow-a { stop-color: #1a3d9a; }
  .panel-offer-glow-b { stop-color: var(--navy-deep); }
  .divider { stroke: var(--white); stroke-width: 9; }
  .brand-mark { fill: var(--sun-yellow); }
  .brand-name {
    font-family: "Archivo Black", "Arial Black", sans-serif;
    font-size: 78px;
    fill: var(--white);
  }
  .headline {
    font-family: "Montserrat", "Arial Black", sans-serif;
    font-weight: 900;
    font-size: 160px;
    letter-spacing: -4px;
    stroke: var(--white);
    stroke-width: 4px;
    paint-order: stroke;
  }
  .headline-tour { fill: var(--sun-yellow); }
  .headline-now { fill: var(--signal-red); }
  .url-band { fill: var(--signal-red); }
  .url-text {
    font-family: "Roboto Condensed", "Arial Narrow", sans-serif;
    font-weight: 800;
    font-size: 66px;
    fill: var(--white);
  }
</style>
</head>
<body>
<main class="canvas">
  <svg class="billboard" viewBox="0 0 1550 420" xmlns="http://www.w3.org/2000/svg" aria-label="Kite &amp; Clover billboard: Tour now">
    <defs>
      <linearGradient id="photo-tones" x1="0" y1="0" x2="1" y2="1">
        <stop offset="0" class="panel-photo-stop-c"/>
        <stop offset="0.45" class="panel-photo-stop-b"/>
        <stop offset="1" class="panel-photo-stop-a"/>
      </linearGradient>
      <radialGradient id="offer-glow" cx="0.55" cy="0.35" r="0.8">
        <stop offset="0" class="panel-offer-glow-a"/>
        <stop offset="1" class="panel-offer-glow-b"/>
      </radialGradient>
    </defs>

    <rect class="panel-brand" x="0" y="0" width="1550" height="420"/>

    <g class="panel-photo" role="img" aria-label="Photo of young children in sun hats playing with a bucket and spade in a sandpit">
      <polygon points="0,0 379,0 504,420 0,420" fill="url(#photo-tones)"/>
    </g>

    <line class="divider" x1="434" y1="140" x2="526" y2="420"/>

    <polygon class="panel-offer" points="984,0 1550,0 1550,420 1104,420" fill="url(#offer-glow)"/>
    <line class="divider" x1="960" y1="0" x2="1086" y2="420"/>

    <g class="brand">
      <circle class="brand-mark" cx="740" cy="125" r="58"/>
      <text class="brand-name" x="740" y="268" text-anchor="middle">Kite &amp;</text>
      <text class="brand-name" x="740" y="350" text-anchor="middle">Clover</text>
    </g>

    <text class="headline headline-tour" x="1496" y="172" text-anchor="end">TOUR</text>
    <text class="headline headline-now" x="1496" y="300" text-anchor="end">NOW</text>

    <polygon class="url-band" points="1016,330 1550,330 1550,400 1039,400"/>
    <text class="url-text" x="1296" y="388" text-anchor="middle" textLength="452" lengthAdjust="spacingAndGlyphs">kiteandclover.edu.au</text>
  </svg>
</main>
</body>
</html>
```